Need new look for home page of Makeup Artist Site

We want a new, clean, modern, professional look for the new design for our website. Our current site is at https://glowvra.com. We would like a high fashion site with diverse ethnic groups represented throughout the page. We like trelk.com as an example of style and user experience. This website is for people to look for a makeup artist or esthetician to come to their home and perform a service there. They will pay on the website and be able to review available service providers and choose one. We will need 2 additional pages once this design is approved. We will pay separately for those.

```html
<!DOCTYPE html>
<html lang="en">
<head>
<meta charset="utf-8">
<title>Glowvra — Beauty &amp; Facial Care at Home</title>
<link href="https://fonts.googleapis.com/css2?family=Noticia+Text:wght@400;700&family=Poppins:wght@400;500&display=swap" rel="stylesheet">
<style>
:root{
  --red:#e21d26;
  --ink:#1d1d1d;
  --body:#6b6b6b;
  --muted:#9a9a9a;
  --line:#e6e6e6;
  --blush:#fbe3df;
  --bg:#ffffff;
}
*{margin:0;padding:0;box-sizing:border-box}
html,body{width:1200px;height:3807px;overflow:hidden;background:var(--bg)}
body{font-family:"Noticia Text",Georgia,serif;color:var(--ink)}
.page{position:relative;width:1200px;height:3807px;overflow:hidden}
.abs{position:absolute}
.sans{font-family:"Poppins",Arial,sans-serif}

/* header */
.brand{font-family:"Noticia Text",Georgia,serif;font-weight:700;font-size:28px;color:var(--red);letter-spacing:1px}
.nav{top:29px;left:290px;display:flex;gap:0;font-family:"Poppins",sans-serif;font-size:11px;font-weight:500;color:var(--ink);letter-spacing:.3px}
.nav span{position:absolute;white-space:nowrap}
.nav .active{color:var(--red)}
.signin{top:29px;left:866px;font-family:"Poppins",sans-serif;font-size:11px;color:var(--red);font-weight:500}
.btn-red{background:var(--red);color:#fff;font-family:"Poppins",sans-serif;font-size:10.5px;font-weight:500;display:flex;align-items:center;justify-content:center;gap:8px;letter-spacing:.3px}
.btn-outline{border:2px solid var(--ink);font-family:"Poppins",sans-serif;font-size:10.5px;font-weight:500;display:flex;align-items:center;justify-content:center;gap:10px;color:var(--ink)}
.btn-outline.red{border-color:var(--red);color:var(--red)}

.photo{display:block}
.hero-title{left:161px;top:205px;font-size:41px;line-height:48px;font-weight:400;color:var(--ink)}
.eyebrow{font-size:13px;color:var(--muted)}
.section-title{font-size:36px;font-weight:400;color:var(--ink)}
.center{text-align:center;left:0;width:1200px}

.step h3{font-size:18px;font-weight:400;margin:22px 0 18px}
.step p{font-size:12.5px;line-height:21px;color:var(--body)}
.step{width:270px}

.accordion-item{left:609px;width:355px}
.accordion-item h4{position:absolute;left:61px;font-size:15px;font-weight:400}
.accordion-item p{position:absolute;left:61px;font-size:12.5px;line-height:21px;color:var(--body);width:285px}

.checklist{left:161px;top:1797px;width:430px;list-style:none}
.checklist li{position:relative;padding-left:24px;font-size:13px;line-height:24px;color:#333;margin-bottom:12px}
.checklist svg{position:absolute;left:0;top:7px}

.card{width:202px;text-align:center}
.card .img{width:202px;height:164px}
.card h5{font-size:15px;font-weight:400;margin-top:18px}
.card .more{font-family:"Poppins",sans-serif;font-size:10px;color:var(--muted);margin-top:24px;letter-spacing:.5px}
.card.featured{box-shadow:0 6px 24px rgba(0,0,0,.09);height:260px}
.card.featured .more{color:var(--red)}

.quote{left:215px;width:770px;top:3136px;text-align:center;font-size:15.5px;line-height:32px;color:#333}
.author{top:3290px;font-family:"Poppins",sans-serif;font-size:12px;font-weight:500;letter-spacing:1px}

.footer-links{top:3709px;left:423px;font-family:"Poppins",sans-serif;font-size:10.5px;font-weight:500;color:var(--ink)}
.footer-links span{position:absolute;white-space:nowrap}
.fine{font-family:"Poppins",sans-serif;font-size:10px;color:var(--muted);letter-spacing:.3px}
</style>
</head>
<body>
<div class="page">

<!-- Header -->
<header>
  <div class="abs brand" style="left:96px;top:18px">GLOWVRA</div>
  <nav class="abs nav">
    <span class="active" style="left:0">HOME</span>
    <span style="left:68px">OUR SERVICES ▾</span>
    <span style="left:180px">CONSULTANTS ▾</span>
    <span style="left:295px">GLOWVRA STREET ▾</span>
    <span style="left:413px">LOCATIONS</span>
  </nav>
  <div class="abs signin">SIGN IN</div>
  <div class="abs btn-red" style="left:930px;top:21px;width:178px;height:32px">BECOME A CONSULTANT</div>
</header>

<!-- Hero -->
<section>
  <div class="abs photo" role="img" aria-label="Makeup artist applying blush to a client at home by a bright window" style="left:537px;top:75px;width:663px;height:518px;background:linear-gradient(120deg,#f4f4f2 0%,#e9e4df 45%,#cdb7a8 70%,#3a2f2b 100%)"></div>
  <h1 class="abs hero-title">We provide Beauty &amp; Facial<br>Care Services in your Home</h1>
  <div class="abs btn-red" style="left:161px;top:377px;width:135px;height:35px">LEARN MORE
    <svg width="12" height="10" viewBox="0 0 12 10"><path d="M0 5h10M6 1l4 4-4 4" stroke="#fff" stroke-width="1.4" fill="none"/></svg></div>
  <div class="abs" style="left:476px;top:547px;width:60px;height:46px;background:#f1f1f1;display:flex;align-items:center;justify-content:center">
    <svg width="8" height="12" viewBox="0 0 8 12"><path d="M7 1L2 6l5 5" stroke="#bbb" stroke-width="1.4" fill="none"/></svg></div>
  <div class="abs" style="left:536px;top:547px;width:60px;height:46px;background:var(--red);display:flex;align-items:center;justify-content:center">
    <svg width="8" height="12" viewBox="0 0 8 12"><path d="M1 1l5 5-5 5" stroke="#fff" stroke-width="1.4" fill="none"/></svg></div>
  <div class="abs" style="left:161px;top:588px;width:22px;height:4px;background:var(--red)"></div>
  <div class="abs" style="left:188px;top:589px;width:4px;height:3px;background:#ddd"></div>
  <div class="abs" style="left:197px;top:589px;width:4px;height:3px;background:#ddd"></div>
</section>

<!-- For Clients -->
<section>
  <div class="abs center eyebrow" style="top:679px">How Glowvra Works</div>
  <h2 class="abs center section-title" style="top:700px">For Clients</h2>

  <div class="abs step" style="left:171px;top:815px">
    <svg width="56" height="46" viewBox="0 0 56 46"><circle cx="18" cy="26" r="18" fill="var(--blush)"/><g stroke="var(--red)" stroke-width="1.6" fill="none"><rect x="10" y="20" width="16" height="10" rx="2" transform="rotate(-45 18 25)"/><path d="M22 14l8-8 6 6-8 8"/><path d="M30 6l4-4 6 6-4 4"/></g></svg>
    <h3>Explore</h3>
    <p>First, choose from our makeup or facial care services. If you don't see what you're looking for, create your custom look</p>
  </div>
  <div class="abs step" style="left:474px;top:815px">
    <svg width="56" height="46" viewBox="0 0 56 46"><circle cx="18" cy="26" r="18" fill="var(--blush)"/><g stroke="var(--red)" stroke-width="1.6" fill="none"><rect x="4" y="6" width="34" height="34" rx="3"/><path d="M4 14h34M12 2v8M30 2v8"/></g><text x="21" y="34" text-anchor="middle" font-family="Poppins" font-size="15" fill="var(--red)">17</text></svg>
    <h3>Schedule</h3>
    <p>Once you have made your selection, choose from our listing of vetted consultants and schedule the day and time you would like to be Glowvra</p>
  </div>
  <div class="abs step" style="left:780px;top:815px">
    <svg width="56" height="46" viewBox="0 0 56 46"><circle cx="18" cy="26" r="18" fill="var(--blush)"/><g stroke="var(--red)" stroke-width="1.6" fill="none"><path d="M3 22L22 4l19 18"/><path d="M8 18v22h28V18"/><rect x="17" y="27" width="10" height="13"/></g></svg>
    <h3>Pay &amp; Get Glowvra</h3>
    <p>Our Consultant will come to you at the scheduled time in the comfort of your space</p>
  </div>

  <div class="abs btn-outline red" style="left:505px;top:1066px;width:188px;height:38px">EXPLORE MAKEUP LOOKS
    <svg width="12" height="10" viewBox="0 0 12 10"><path d="M0 5h10M6 1l4 4-4 4" stroke="currentColor" stroke-width="1.4" fill="none"/></svg></div>
</section>

<!-- For Consultants -->
<section>
  <div class="abs photo" role="img" aria-label="Desk calendar with a smartphone showing an appointments app, plant and pen" style="left:0;top:1233px;width:539px;height:379px;background:linear-gradient(135deg,#e9e5de 0%,#f7f6f3 40%,#eceae6 70%,#d9d6d0 100%)"></div>
  <div class="abs eyebrow" style="left:610px;top:1232px">How Glowvra Works</div>
  <h2 class="abs section-title" style="left:610px;top:1253px">For Consultants</h2>

  <div class="abs accordion-item" style="top:1338px">
    <svg width="40" height="34" viewBox="0 0 40 34"><circle cx="14" cy="18" r="13" fill="var(--blush)"/><g stroke="#333" stroke-width="1.3" fill="none"><circle cx="12" cy="10" r="4"/><circle cx="26" cy="10" r="4"/><circle cx="19" cy="16" r="4"/><path d="M4 28c0-6 4-10 8-10M34 28c0-6-4-10-8-10M11 32c0-6 4-10 8-10s8 4 8 10"/></g></svg>
    <h4 style="top:6px">Build Your Client Base</h4>
    <svg class="abs" style="left:344px;top:12px" width="10" height="6" viewBox="0 0 10 6"><path d="M1 1l4 4 4-4" stroke="#333" stroke-width="1.4" fill="none"/></svg>
  </div>
  <div class="abs accordion-item" style="top:1396px">
    <svg width="40" height="34" viewBox="0 0 40 34"><circle cx="14" cy="18" r="13" fill="var(--blush)"/><g stroke="#333" stroke-width="1.3" fill="none"><rect x="4" y="4" width="30" height="26" rx="2"/><path d="M4 11h30M10 1v6M28 1v6M12 22l5 4 10-10"/></g></svg>
    <h4 style="top:6px">Manage your Business</h4>
    <svg class="abs" style="left:344px;top:12px" width="10" height="6" viewBox="0 0 10 6"><path d="M1 5l4-4 4 4" stroke="#333" stroke-width="1.4" fill="none"/></svg>
    <p style="top:38px">You're always in control of your hours and your appointments</p>
  </div>
  <div class="abs accordion-item" style="top:1498px">
    <svg width="40" height="36" viewBox="0 0 40 36"><circle cx="14" cy="20" r="13" fill="var(--blush)"/><g stroke="#333" stroke-width="1.3" fill="none"><rect x="4" y="6" width="18" height="16" rx="2"/><path d="M4 11h18"/><rect x="14" y="14" width="18" height="20" rx="2"/><path d="M18 21h10M18 26h10M18 31h6"/><circle cx="30" cy="8" r="6"/><path d="M30 5v3h3"/></g></svg>
    <h4 style="top:8px">Check Appointments and Go!</h4>
    <svg class="abs" style="left:344px;top:14px" width="10" height="6" viewBox="0 0 10 6"><path d="M1 1l4 4 4-4" stroke="#333" stroke-width="1.4" fill="none"/></svg>
  </div>

  <div class="abs btn-outline" style="left:610px;top:1575px;width:190px;height:37px">JOIN GLOWVRA NETWORK
    <svg width="12" height="10" viewBox="0 0 12 10"><path d="M0 5h10M6 1l4 4-4 4" stroke="currentColor" stroke-width="1.4" fill="none"/></svg></div>
</section>

<!-- Why -->
<section>
  <div class="abs eyebrow" style="left:161px;top:1703px">What makes us great</div>
  <h2 class="abs section-title" style="left:161px;top:1724px">Why Glowvra</h2>
  <ul class="abs checklist">
    <li><svg width="12" height="10" viewBox="0 0 12 10"><path d="M1 5l3.5 3.5L11 1" stroke="var(--red)" stroke-width="1.6" fill="none"/></svg>Access to service of the Washington Metropolitan area's most qualified and vetted professional makeup artists and estheticians.</li>
    <li><svg width="12" height="10" viewBox="0 0 12 10"><path d="M1 5l3.5 3.5L11 1" stroke="var(--red)" stroke-width="1.6" fill="none"/></svg>Convenience of having your makeup done in your home or at a location of your choosing.</li>
    <li><svg width="12" height="10" viewBox="0 0 12 10"><path d="M1 5l3.5 3.5L11 1" stroke="var(--red)" stroke-width="1.6" fill="none"/></svg>Sessions booked according to your schedule.</li>
    <li><svg width="12" height="10" viewBox="0 0 12 10"><path d="M1 5l3.5 3.5L11 1" stroke="var(--red)" stroke-width="1.6" fill="none"/></svg>Select the look that you want for any occasion.</li>
    <li><svg width="12" height="10" viewBox="0 0 12 10"><path d="M1 5l3.5 3.5L11 1" stroke="var(--red)" stroke-width="1.6" fill="none"/></svg>Preliminary test run included for your most important events.</li>
    <li><svg width="12" height="10" viewBox="0 0 12 10"><path d="M1 5l3.5 3.5L11 1" stroke="var(--red)" stroke-width="1.6" fill="none"/></svg>Access to Glowvra Street's blogs, tips, trends and makeup events.</li>
  </ul>
  <div class="abs photo" role="img" aria-label="Fashion portrait of a model with a bold red paint stroke across the eyes" style="left:622px;top:1700px;width:578px;height:390px;background:linear-gradient(90deg,#dcdad8 0%,#d6d3d0 45%,#b98a6e 75%,#6b4635 100%)"></div>
</section>

<!-- Services -->
<section>
  <div class="abs center eyebrow" style="top:2197px">What we offer</div>
  <h2 class="abs center section-title" style="top:2219px">Our Services</h2>

  <div class="abs card featured" style="left:161px;top:2316px">
    <div class="img" role="img" aria-label="Bride with elegant updo and hair jewel" style="background:linear-gradient(135deg,#3b2a22,#8a6550 60,#e8e2dc)"></div>
    <h5>Weddings</h5><div class="more">LEARN MORE ›</div>
  </div>
  <div class="abs card" style="left:386px;top:2316px">
    <div class="img" role="img" aria-label="Makeup artist applying makeup to a seated client" style="background:linear-gradient(135deg,#ece9e6,#cbbfb5 60%,#5a4a42)"></div>
    <h5>Full Makeup Application</h5><div class="more">LEARN MORE ›</div>
  </div>
  <div class="abs card" style="left:610px;top:2316px">
    <div class="img" role="img" aria-label="Gift card tied with a red ribbon bow" style="background:linear-gradient(160deg,#ffffff,#f0f0f0 55%,#e3b4b4)"></div>
    <h5>Gift Certificates</h5><div class="more">LEARN MORE ›</div>
  </div>
  <div class="abs card" style="left:835px;top:2316px">
    <div class="img" role="img" aria-label="Group of three smiling women in white tops" style="background:linear-gradient(90deg,#cfb6a4,#efe9e4 50%,#c7a890)"></div>
    <h5>Group Party</h5><div class="more">LEARN MORE ›</div>
  </div>

  <div class="abs card" style="left:161px;top:2627px">
    <div class="img" role="img" aria-label="Woman touching her glowing skin after a facial" style="background:linear-gradient(90deg,#ffffff 20%,#5a3a2c 60%,#2a1a14)"></div>
    <h5>Facial Care Services</h5><div class="more">LEARN MORE ›</div>
  </div>
  <div class="abs card" style="left:386px;top:2627px">
    <div class="img" role="img" aria-label="Makeup brush applying powder in a close-up beauty shot" style="background:linear-gradient(135deg,#ffffff,#f2ddd3 55%,#d9a892)"></div>
    <h5>Beauty Tutorials</h5><div class="more">LEARN MORE ›</div>
  </div>
  <div class="abs card" style="left:610px;top:2627px">
    <div class="img" role="img" aria-label="Well-groomed man in a close-up portrait" style="background:linear-gradient(135deg,#8d8c88,#c9a994 55%,#4d4540)"></div>
    <h5>Men's Grooming</h5><div class="more">LEARN MORE ›</div>
  </div>
  <div class="abs card" style="left:835px;top:2627px">
    <div class="img" role="img" aria-label="Model on a film set with a clapperboard" style="background:linear-gradient(135deg,#6b4a36,#b47b55 50%,#2e4d5a)"></div>
    <h5>Commercial Contracts</h5><div class="more">LEARN MORE ›</div>
  </div>
</section>

<!-- Testimonials -->
<section>
  <div class="abs center eyebrow" style="top:2994px">What They Say About Us</div>
  <h2 class="abs center section-title" style="top:3016px">Testimonials</h2>
  <div class="abs" style="left:216px;top:3112px;font-size:64px;line-height:1;color:#f5c9c3;font-family:Georgia,serif">“</div>
  <p class="abs quote">To say the least we were thrilled with Glowvra and the artist they provided. The day of my wedding the artist arrived right on schedule and did a great job getting me and my bridesmaids ready. My makeup looked amazing making my husband cry at first sight of me that day. Thank you to Glowvra for providing such competent and talented people</p>
  <div class="abs center author">MARA DELANE</div>
</section>

<!-- CTA band -->
<section>
  <div class="abs" role="img" aria-label="Pink illustrated pattern of leaves and cosmetic bottles" style="left:0;top:3390px;width:1200px;height:271px;background:linear-gradient(180deg,#f9e2de 0%,#f8d9d3 60%,#f4c8bf 100%)"></div>
  <div class="abs center" style="top:3535px;font-size:32px;color:#333">Go ahead and revel in your Glowvra experience!</div>
  <div class="abs center sans" style="top:3608px;font-size:11px;color:var(--red);letter-spacing:.8px">GET STARTED NOW! ›</div>
</section>

<!-- Footer -->
<footer>
  <div class="abs brand" style="left:161px;top:3697px">GLOWVRA</div>
  <div class="abs footer-links">
    <span style="left:0">ABOUT US</span>
    <span style="left:77px">SUPPORT</span>
    <span style="left:148px">FAQS</span>
    <span style="left:199px">LOST &amp; FOUND</span>
    <span style="left:302px">USER AGREEMENT</span>
    <span style="left:419px">GLOWVRA STREET</span>
    <span style="left:524px">TIP CONSULTANT</span>
  </div>
  <div class="abs fine" style="left:161px;top:3775px">© 2019 ALL RIGHTS RESERVED</div>
  <div class="abs fine" style="left:893px;top:3775px">FOLLOW US ON</div>
  <div class="abs" style="left:995px;top:3773px;width:11px;height:11px;background:#8a8a8a"></div>
  <div class="abs" style="left:1025px;top:3773px;width:11px;height:11px;border:1.5px solid var(--red);border-radius:3px"></div>
</footer>

</div>
</body>
</html>
```